Presentation and Communication Coaching Services Business needs updated interactive web site

I want to keep the color scheme, functionality, and pages of my current site, but with a newer/updated look. I need to improve security and simplify images, etc. (Please see current site http://brackleyvoicementor.com ) This will need be functional on mobile devices, as well.

I'm attached to the scrolling client list and scrolling client feedback.

Industry/Entity Type

Professional Service

Font styles to use
Sans Serif

Colors
0356a4
f37122
33a6d7

Requirements
Must have
• scrolling client banner on home page, client comments slider, color scheme
• Please see current site: http://brackleyvoicementor.com
Nice to have
• better action/appearance
Should not have
• I don't want it to look like all the other sites/templates

```html
<!DOCTYPE html>
<html lang="en">
<head>
<meta charset="utf-8">
<title>Brackley Voice Mentor — Services</title>
<link rel="stylesheet" href="https://fonts.googleapis.com/css2?family=Montserrat:wght@500;600;700&display=swap">
<style>
  :root {
    --blue: #0356a4;
    --orange: #f37122;
    --sky: #33a6d7;
    --white: #ffffff;
    --ink: #15181f;
    --ink-2: #252a35;
  }
  * { box-sizing: border-box; margin: 0; padding: 0; }
  html, body { width: 1153px; height: 1200px; overflow: hidden; }
  body {
    position: relative;
    background: var(--white);
    font-family: "Montserrat", Arial, sans-serif;
    color: var(--white);
  }

  .services-title {
    position: absolute; top: 54px; left: 0; width: 100%;
    text-align: center; color: var(--blue);
    font-size: 23px; font-weight: 700; letter-spacing: 0.5px;
  }

  .service-card {
    position: absolute; width: 512px; height: 270px;
    background: var(--blue); border-radius: 88px;
    overflow: hidden;
    box-shadow: 0 8px 14px rgba(0, 0, 0, 0.28);
  }
  .card-1 { left: 57px;  top: 116px; }
  .card-2 { left: 585px; top: 116px; }
  .card-3 { left: 57px;  top: 414px; }
  .card-4 { left: 585px; top: 414px; }

  .service-number {
    position: absolute; width: 192px;
    background: var(--orange);
    display: flex; align-items: center; justify-content: center;
    font-size: 82px; font-weight: 600; letter-spacing: 1px; line-height: 1;
  }
  .card-1 .service-number { left: 320px; top: 101px; height: 169px; border-top-left-radius: 130px 110px; }
  .card-2 .service-number { left: 0;     top: 101px; height: 169px; border-top-right-radius: 130px 110px; }
  .card-3 .service-number { left: 320px; top: 0;     height: 167px; border-bottom-left-radius: 130px 110px; }
  .card-4 .service-number { left: 0;     top: 0;     height: 167px; border-bottom-right-radius: 130px 110px; }

  .service-name {
    position: absolute;
    font-size: 40px; font-weight: 600; line-height: 46px; letter-spacing: 0;
    text-transform: uppercase;
  }
  .service-text {
    position: absolute;
    font-size: 12px; font-weight: 600; line-height: 21px;
    text-transform: uppercase;
  }
  .card-1 .service-name { left: 67px;  top: 54px; }
  .card-1 .service-text { left: 38px;  top: 139px; width: 300px; }
  .card-2 .service-name { left: 217px; top: 52px; }
  .card-2 .service-text { left: 209px; top: 171px; width: 290px; }
  .card-3 .service-name { left: 63px;  top: 40px; }
  .card-3 .service-text { left: 59px;  top: 157px; width: 300px; }
  .card-4 .service-name { left: 227px; top: 40px; }
  .card-4 .service-text { left: 197px; top: 153px; width: 290px; }

  .publications {
    position: absolute; left: 0; top: 746px; width: 1153px; height: 454px;
    background:
      linear-gradient(160deg, transparent 30%, rgba(255,255,255,0.05) 45%, transparent 60%),
      linear-gradient(180deg, var(--ink-2) 0%, var(--ink) 100%);
  }
  .publications-title {
    position: absolute; top: 44px; left: 0; width: 100%;
    text-align: center; font-size: 23px; font-weight: 700; letter-spacing: 0.5px;
  }
  .pub-label {
    position: absolute; top: 106px; width: 283px; height: 36px;
    border-radius: 18px; background: var(--orange);
    display: flex; align-items: center; justify-content: center;
    font-size: 11px; font-weight: 700; text-transform: uppercase;
    box-shadow: 0 4px 8px rgba(0,0,0,0.4);
  }
  .pub-cover { position: absolute; }
  .cover-1 { left: 121px; top: 158px; width: 211px; height: 268px; background: linear-gradient(180deg, #2ab0e0, #1a8fc4); }
  .cover-2 { left: 471px; top: 155px; width: 211px; height: 270px; background: linear-gradient(180deg, #6fa7d6, #a9cce8 60%, #d8e4ee); }
  .cover-3 { left: 801px; top: 156px; width: 273px; height: 265px; background: linear-gradient(180deg, #8a1f1a, #3a2a24 70%, #1e1d1d); }
</style>
</head>
<body>
  <h2 class="services-title">OUR SERVICES</h2>

  <section class="service-card card-1">
    <h3 class="service-name">Coaching</h3>
    <p class="service-text">One-on-one, individual, and customized to your unique goals, obstacles, and challenges.<br>In person, or via videoconference.</p>
    <div class="service-number">01</div>
  </section>

  <section class="service-card card-2">
    <div class="service-number">02</div>
    <h3 class="service-name">Accents</h3>
    <p class="service-text">Unique, effective program design and facilitation to match the needs of executivess, managers, or promising individuals of any level.</p>
  </section>

  <section class="service-card card-3">
    <h3 class="service-name">Coustom<br>Workshop</h3>
    <p class="service-text">Unique, effective program design and facilitation to match the needs of executivess, managers, or promising individuals of any level.</p>
    <div class="service-number">03</div>
  </section>

  <section class="service-card card-4">
    <div class="service-number">04</div>
    <h3 class="service-name">Keynote<br>Speecher</h3>
    <p class="service-text">Support for executives from outside the U.S. to increase intelligibility and diminish obstacles to successful communication in American English.</p>
  </section>

  <section class="publications">
    <h2 class="publications-title">RECENT PUBLICATIONS</h2>

    <div class="pub-label" style="left:81px;">Spring/Summer Dapper Style Guide</div>
    <div class="pub-cover cover-1" role="img" aria-label="Magazine cover of the spring/summer style guide issue"></div>

    <div class="pub-label" style="left:435px;">Maison Belle Magazine</div>
    <div class="pub-cover cover-2" role="img" aria-label="Magazine cover featuring a cover star in a blue dress"></div>

    <div class="pub-label" style="left:796px;">Metro City Post</div>
    <div class="pub-cover cover-3" role="img" aria-label="Photo of a surprised speaker in a suit behind a row of microphones before a red curtain"></div>
  </section>
</body>
</html>
```